New Architectural Firm Business Cards

New Business card to compliment previous pixel forum logo (attached). Please design a business card that is simple, modern, creative....please do not use "symbols", simply the logo and associated graphics/text. The front should contain name/address/phone/email/web address (with graphics).....back should be 100% graphic design using the logo somehow. Hoping for a two color (black and yellow) design. full bleed design, no borders

Target Market(s)

Commercial Architecture Clients

Industry/Entity Type

Architecture

Contact Information for Business Card

Please design a business card that is simple, modern, creative....please do not use "symbols", simply the logo and associated graphics/text. The front should contain name/address/phone/email/web address (with graphics).....back should be 100% graphic design using the logo somehow

Font styles to use
Sans Serif

Colors
FFF300
FFF600
FEFA6F
FFFEC7
FFFEE8

Requirements
Must have
• Clean, Modern Design
Should not have
• Stock images or "icons"

```html
<!DOCTYPE html>
<html lang="en">
<head>
<meta charset="utf-8">
<title>Halvern Architecture – Business Card</title>
<link rel="stylesheet" href="https://fonts.googleapis.com/css2?family=Archivo:wght@400;500;600&family=Work+Sans:wght@500&display=swap">
<style>
  :root {
    --page-bg: #d4d5d7;
    --card-dark: #232323;
    --card-light: #ffffff;
    --brand-yellow: #f5c211;
    --ink: #1e1e1e;
    --shadow: rgba(0, 0, 0, 0.28);
  }
  * { box-sizing: border-box; margin: 0; padding: 0; }
  html, body {
    width: 1138px;
    height: 1200px;
    overflow: hidden;
    background: var(--page-bg);
  }
  .sheet {
    width: 1138px;
    height: 1200px;
    display: flex;
    flex-direction: column;
    align-items: center;
    justify-content: center;
    gap: 90px;
  }
  .card {
    position: relative;
    width: 700px;
    height: 400px;
    border-radius: 14px;
    box-shadow: 4px 6px 10px var(--shadow);
    overflow: hidden;
  }

  /* Back side */
  .card--back { background: var(--card-dark); }
  .back-mark {
    position: absolute;
    left: 40px;
    bottom: 90px;
    width: 150px;
    height: 150px;
    background: #2e2e2e;
  }
  .back-name {
    position: absolute;
    right: 24px;
    bottom: 88px;
    font-family: "Archivo", sans-serif;
    font-weight: 500;
    font-size: 46px;
    letter-spacing: 0.5px;
    color: var(--brand-yellow);
    line-height: 1;
  }

  /* Front side */
  .card--front { background: var(--card-light); }
  .front-brand {
    position: absolute;
    top: 52px;
    right: 46px;
    display: flex;
    align-items: center;
    gap: 12px;
  }
  .front-brand__square {
    width: 22px;
    height: 22px;
    background: var(--brand-yellow);
  }
  .front-brand__name {
    font-family: "Archivo", sans-serif;
    font-weight: 600;
    font-size: 24px;
    line-height: 1.1;
    color: var(--brand-yellow);
    text-align: right;
  }
  .person {
    position: absolute;
    left: 47px;
    top: 206px;
    font-family: "Archivo", sans-serif;
  }
  .person__name {
    font-weight: 500;
    font-size: 26px;
    letter-spacing: 0.6px;
    color: var(--brand-yellow);
    line-height: 1;
  }
  .person__role {
    margin-top: 10px;
    font-family: "Work Sans", sans-serif;
    font-weight: 500;
    font-size: 13px;
    letter-spacing: 1px;
    color: var(--ink);
  }
  .contact {
    position: absolute;
    left: 47px;
    top: 290px;
    display: flex;
    align-items: flex-end;
    font-family: "Work Sans", sans-serif;
    font-weight: 500;
    font-size: 14px;
    letter-spacing: 0.7px;
    color: var(--ink);
    line-height: 28px;
  }
  .contact__lines { width: 230px; }
  .contact__divider {
    width: 4px;
    height: 50px;
    background: var(--brand-yellow);
    margin: 0 20px 4px 0;
  }
  .contact__address { margin-bottom: 1px; }
</style>
</head>
<body>
  <main class="sheet">
    <section class="card card--back" aria-label="Card back">
      <div class="back-mark"></div>
      <p class="back-name">HALVERN ARCHITECTURE</p>
    </section>

    <section class="card card--front" aria-label="Card front">
      <div class="front-brand">
        <span class="front-brand__square"></span>
        <p class="front-brand__name">HALVERN<br>ARCHITECTURE</p>
      </div>

      <div class="person">
        <h1 class="person__name">OWEN TARRANT</h1>
        <p class="person__role">C.E.O</p>
      </div>

      <div class="contact">
        <div class="contact__lines">
          <p>555-018-4420</p>
          <p>hello@halvernarch.com</p>
          <p>www.halvernarch.com</p>
        </div>
        <span class="contact__divider"></span>
        <div class="contact__address">
          <p>140 Ridgeline Ave</p>
          <p>Ashford, GA 30000</p>
        </div>
      </div>
    </section>
  </main>
</body>
</html>
```